Harrowden Metal recycling, a business card/logo for our industrial family metal recycling company

A new business card design/logo for our long established family metal recycling company.
I have a logo for our property company which was designed a few months ago on pixel forge which I would like to be very close to this design but have a more industrial feel to it and in a darker blue colour, please see attachments.

Target Market(s)

industries that produce metal waste for recycling, construction sites, engineering companies, manufactures, builders, plumbers, electricians, general house holders.

Industry/Entity Type

Recycling

Contact Information for Business Card

owner/director...Martin harrowden
e-mail....info@harrowdenscrapworks.co.uk
web address.....harrowdenscrapworks.co.uk

Font styles to use
Serif
Sans Serif

Colors
0255a3
ffffff

Requirements
Must have
• -dark blue business card on front.
-white on the back, see contact details, e-mail address for metal company.
-to have an industrial feel to it.
-harrowden logo as business card attached but (harrowden metal recycling)
please remove the little roof/arrow above harrowden as this was relevant to property company.
Nice to have
• please see our website harrowdenscrapworks.co.uk with all details
being correct however I would like to refresh the logo to more like the harrowden property investment business card logo attached.
Should not have
• should not contain details from property investments card as this design is for the metal recycling company.

```html
<!DOCTYPE html>
<html lang="en">
<head>
<meta charset="utf-8">
<title>Harrowden Metal Recycling – Business Card</title>
<link rel="stylesheet" href="https://fonts.googleapis.com/css2?family=Barlow+Condensed:wght@600&family=Poppins:wght@300&display=swap">
<style>
  :root {
    --backdrop: #1e1e1e;
    --card-blue: #273a7c;
    --ink-white: #ffffff;
    --ink-grey: #a3a6b3;
  }
  * { box-sizing: border-box; margin: 0; padding: 0; }
  html, body { width: 1200px; height: 900px; overflow: hidden; }
  body {
    background: var(--backdrop);
    display: flex;
    flex-direction: column;
    align-items: center;
    justify-content: center;
    gap: 40px;
  }
  .card {
    position: relative;
    width: 700px;
    height: 400px;
    background: var(--card-blue);
    color: var(--ink-white);
  }
  .brand-name {
    font-family: "Barlow Condensed", sans-serif;
    font-weight: 600;
    font-size: 44px;
    letter-spacing: 3px;
    text-transform: uppercase;
    color: var(--ink-white);
    text-align: center;
    white-space: nowrap;
  }
  .card-front { display: flex; align-items: center; justify-content: center; }
  .card-back .brand-name {
    position: absolute;
    top: 72px; left: 0; right: 0;
  }
  .rule {
    position: absolute;
    top: 190px; left: 60px; right: 60px;
    height: 1px;
    background: var(--ink-white);
  }
  .contact-block {
    position: absolute;
    top: 262px; left: 60px; right: 40px;
    display: flex;
    align-items: center;
  }
  .person { text-align: right; width: 250px; }
  .person-name {
    font-family: "Barlow Condensed", sans-serif;
    font-weight: 600;
    font-size: 34px;
    line-height: 1.05;
  }
  .person-role {
    font-family: "Poppins", sans-serif;
    font-weight: 300;
    font-size: 17px;
    color: var(--ink-grey);
  }
  .divider {
    width: 2px; height: 78px;
    background: var(--ink-white);
    margin: 0 22px;
  }
  .contact-list { list-style: none; }
  .contact-list li {
    display: flex;
    align-items: center;
    gap: 10px;
    font-family: "Poppins", sans-serif;
    font-weight: 300;
    font-size: 17px;
    color: var(--ink-grey);
    line-height: 27px;
  }
  .contact-list svg { width: 18px; height: 18px; flex: none; }
</style>
</head>
<body>
  <section class="card card-front">
    <p class="brand-name">Harrowden Metal Recycling</p>
  </section>

  <section class="card card-back">
    <p class="brand-name">Harrowden Metal Recycling</p>
    <div class="rule"></div>
    <div class="contact-block">
      <div class="person">
        <p class="person-name">Martin harrowden</p>
        <p class="person-role">Owner/Director</p>
      </div>
      <div class="divider"></div>
      <ul class="contact-list">
        <li>
          <svg viewBox="0 0 24 24" fill="none" stroke="#ffffff" stroke-width="1.8" stroke-linejoin="round">
            <circle cx="12" cy="12" r="10"/>
            <path d="M8.5 7.5l2 2-1 1.5c.8 1.6 1.9 2.7 3.5 3.5l1.5-1 2 2-1.2 1.3c-3.5-.3-7.3-4.1-7.6-7.6z"/>
          </svg>
          020-7946-0381
        </li>
        <li>
          <svg viewBox="0 0 24 24" fill="none" stroke="#ffffff" stroke-width="1.8" stroke-linejoin="round">
            <rect x="3" y="6" width="18" height="12"/>
            <path d="M3 6l9 7 9-7"/>
          </svg>
          info@harrowdenscrapworks.co.uk
        </li>
        <li>
          <svg viewBox="0 0 24 24" fill="none" stroke="#ffffff" stroke-width="1.8">
            <circle cx="12" cy="12" r="9"/>
            <ellipse cx="12" cy="12" rx="4" ry="9"/>
            <path d="M3 12h18M5 7.5h14M5 16.5h14"/>
          </svg>
          www.harrowdenscrapworks.co.uk
        </li>
      </ul>
    </div>
  </section>
</body>
</html>
```